Corporate identity and pre-opening design for a brand new Casino

Dear designers!

We need a design for the pre-opening ad campaign of our brand new casino called "Velmora Casino" and planned to open soon.
It is situated in "Ostrel Lodge Ruzhan" – a 4-star luxury and business hotel, located in the city of Plovdiv, Bulgaria.
Our vision of the project is bold, but stylish and elegant. We desire to see uniqueness by all means.
Our slogan is “So many ways to have fun”.
We need a design for our ad campaign for ex. billbord 8m x 4m. We expect your elegant and creative designs. We are trying to avoid the conventional, but at the same time we do not want to be too extravagant.

Thank you and good luck!

Requirements
Should not have
• dices

```html
<!DOCTYPE html>
<html lang="en">
<head>
<meta charset="utf-8">
<title>Velmora Casino – Open Soon Billboard</title>
<link rel="stylesheet" href="https://fonts.googleapis.com/css2?family=Bowlby+One&family=Oswald:wght@500;600&display=swap">
<style>
  :root{
    --page:#4b4b4b;
    --navy-deep:#0b1433;
    --navy:#1b2a5e;
    --navy-glow:#2d4590;
    --red:#c8102e;
    --red-dark:#7d0a1c;
    --gold:#f3c64a;
    --gold-dark:#a87a1c;
    --white:#ffffff;
  }
  *{box-sizing:border-box;margin:0;padding:0}
  html,body{width:720px;height:1200px;overflow:hidden}
  body{background:var(--page);position:relative;font-family:"Oswald",sans-serif}

  .billboard{
    position:absolute;left:20px;top:430px;width:680px;height:340px;
    background:radial-gradient(ellipse at 45% 40%,var(--navy-glow) 0%,var(--navy) 40%,var(--navy-deep) 100%);
    overflow:hidden;
  }
  .scatter{
    position:absolute;inset:30px 40px 90px 40px;
    background:radial-gradient(ellipse at 50% 45%,rgba(243,198,74,.10) 0%,rgba(243,198,74,0) 70%);
  }
  .brand{
    position:absolute;right:28px;top:22px;display:flex;align-items:center;gap:8px;
    color:var(--white);font-weight:500;font-size:15px;letter-spacing:1px;text-transform:uppercase;
  }
  .brand-dot{width:16px;height:16px;border-radius:50%;background:var(--white)}

  .headline{
    position:absolute;left:150px;top:44px;width:330px;height:80px;border-radius:40px;
    background:linear-gradient(180deg,#e8213f 0%,var(--red) 50%,var(--red-dark) 100%);
    border:4px solid var(--gold);
    box-shadow:0 0 0 2px var(--gold-dark),0 6px 14px rgba(0,0,0,.5);
    display:flex;align-items:flex-start;justify-content:center;padding-top:8px;
  }
  .headline h1{
    font-family:"Bowlby One",sans-serif;font-weight:400;font-size:40px;line-height:1;
    color:var(--gold);letter-spacing:1px;
  }
  .slot-machine{
    position:absolute;left:276px;top:106px;width:80px;height:54px;border-radius:10px;
    background:linear-gradient(180deg,#e9e9e9 0%,#9b9b9b 100%);
    border:3px solid var(--gold);
  }
  .tagline{
    position:absolute;left:0;right:0;top:170px;text-align:center;
    color:var(--white);font-weight:500;font-size:22px;line-height:1.2;letter-spacing:1.5px;
  }
  .location{
    position:absolute;left:84px;top:222px;width:492px;height:40px;border-radius:20px;
    background:linear-gradient(180deg,#d81a36 0%,var(--red-dark) 100%);
    border:2px solid var(--gold);
    display:flex;align-items:center;gap:12px;padding-left:12px;
    color:var(--white);font-weight:600;font-size:15px;letter-spacing:.5px;
  }
  .location svg{flex:none}
</style>
</head>
<body>
  <section class="billboard" aria-label="Velmora Casino open soon billboard">
    <div class="scatter" role="img" aria-label="Scattered gold coins and casino chips"></div>

    <div class="brand"><span class="brand-dot"></span>Velmora Casino</div>

    <div class="headline"><h1>OPEN SOON</h1></div>
    <div class="slot-machine" role="img" aria-label="Slot machine reels"></div>

    <p class="tagline">SO MANY WAYS TO HAVE FUN</p>

    <div class="location">
      <svg width="24" height="24" viewBox="0 0 24 24" aria-hidden="true">
        <circle cx="12" cy="12" r="11" fill="#f3c64a"/>
        <path d="M12 5a4.5 4.5 0 0 0-4.5 4.5c0 3.4 4.5 8.5 4.5 8.5s4.5-5.1 4.5-8.5A4.5 4.5 0 0 0 12 5z" fill="#c8102e"/>
        <circle cx="12" cy="9.5" r="1.7" fill="#f3c64a"/>
      </svg>
      OSTREL LODGE RUZHAN, CITY OF PLOVDIV, BULGARIA
    </div>
  </section>
</body>
</html>
```